Larkfield Compliance Partners - Invitation for a get together

We are in need of an invitation for an upcoming gathering we are having with our clients. The gathering will be in Tobin's Bar in Manly. http://www.tobinsbar.example/. Tobins bar is described as a New York loft style bar.

We are a building and construction consulting firm, our clients include firms such as Grevo Pike, Osprey Vale, Caldrik.

We are seeking to thank our clients for their support with a Friday afternoon drinks at Tobins Bar. We will be providing food and drinks.

Details are:-

When - Friday 19 September 2014
Time - 4pm onwards
Where - 12 Quarry Row Manly

I would like a map to appear on the invite indicating where the bar is. I would also like

Target Market(s)

Clients, such as property developers, architects, builders

Industry/Entity Type

Construction

Colors

Designer to choose colors to be used in the design.

Requirements
Must have
• Details of what the invite is for, i.e. Larkfield Compliance Partners invites you to Tobins Bar at Manly for a casual drink and get together.

Details of the event i.e. Date, time, Location
Nice to have
• We hope the invite will have a sophisticated feel about it, like a trendy New York bar

```html
<!DOCTYPE html>
<html lang="en">
<head>
<meta charset="utf-8">
<title>Larkfield Compliance Partners – Invitation</title>
<link rel="stylesheet" href="https://fonts.googleapis.com/css2?family=Great+Vibes&family=Poiret+One&display=swap">
<style>
  :root {
    --page: #ffffff;
    --card-dark: #111111;
    --card-mid: #1c1c1c;
    --glow: rgba(150, 20, 20, 0.55);
    --ink: #f4f4f4;
  }
  * { box-sizing: border-box; margin: 0; padding: 0; }
  html, body {
    width: 1200px; height: 1000px; overflow: hidden;
    background: var(--page);
  }
  .invitation {
    position: absolute; left: 162px; top: 172px;
    width: 875px; height: 656px; overflow: hidden;
    color: var(--ink);
    font-family: "Poiret One", "Quicksand", sans-serif;
  }
  .invitation__backdrop {
    position: absolute; inset: 0; width: 100%; height: 100%;
  }
  .invitation__lead {
    position: absolute; top: 8px; left: 0; width: 100%;
    text-align: center;
    font-family: "Great Vibes", cursive;
    font-size: 40px; line-height: 1;
  }
  .invitation__host {
    position: absolute; top: 82px; left: 0; width: 100%;
    text-align: center;
    font-size: 92px; line-height: 1; letter-spacing: 2px;
  }
  .invitation__host-sub {
    position: absolute; top: 206px; right: 29px;
    font-size: 50px; line-height: 1;
  }
  .invitation__message {
    position: absolute; top: 336px; left: 0; width: 100%;
    padding-left: 30px; text-align: center;
    font-size: 35px; line-height: 1; letter-spacing: 0.5px;
  }
  .details {
    position: absolute; top: 458px; left: 0; width: 100%;
  }
  .details__item {
    position: absolute; top: 0; width: 260px; margin-left: -130px;
    text-align: center;
  }
  .details__item--date { left: 139px; }
  .details__item--place { left: 447px; }
  .details__item--contact { left: 734px; }
  .details__label {
    font-size: 37px; line-height: 1; font-weight: 400;
    margin-bottom: 30px;
  }
  .details__text {
    font-size: 21px; line-height: 27px;
  }
</style>
</head>
<body>
  <main class="invitation">
    <svg class="invitation__backdrop" role="img" aria-label="Dark textured loft-bar background with a soft red glow behind the title" viewBox="0 0 875 656" preserveAspectRatio="none">
      <defs>
        <linearGradient id="bg-shade" x1="0" y1="0" x2="0" y2="1">
          <stop offset="0" stop-color="#151515"/>
          <stop offset="0.6" stop-color="#1d1d1d"/>
          <stop offset="1" stop-color="#121212"/>
        </linearGradient>
        <radialGradient id="title-glow" cx="0.5" cy="0.5" r="0.5">
          <stop offset="0" stop-color="var(--glow)"/>
          <stop offset="1" stop-color="rgba(150,20,20,0)"/>
        </radialGradient>
      </defs>
      <rect width="875" height="656" fill="url(#bg-shade)"/>
      <ellipse cx="430" cy="130" rx="300" ry="95" fill="url(#title-glow)"/>
    </svg>

    <p class="invitation__lead">please join us</p>
    <h1 class="invitation__host">LARKFIELD</h1>
    <p class="invitation__host-sub">compliance partners</p>

    <p class="invitation__message">We will be providing food and drinks at Tobins bar</p>

    <section class="details">
      <div class="details__item details__item--date">
        <h2 class="details__label">date</h2>
        <p class="details__text">Friday<br>19 September 2014<br>4pm onwards</p>
      </div>
      <div class="details__item details__item--place">
        <h2 class="details__label">place</h2>
        <p class="details__text">12 Quarry<br>Row Manly</p>
      </div>
      <div class="details__item details__item--contact">
        <h2 class="details__label">contact</h2>
        <p class="details__text">(02) 5550-1420<br>tobinsbar.example</p>
      </div>
    </section>
  </main>
</body>
</html>
```